AMAZING WEBSITE DESIGN NEEDED FOR MAID / CLEANING SERVICE

NOTE: This is Website Design Only - No coding required

Please submit your designs ASAP as we want to pick a winner and get started!

Hey,

We are looking for a new amazing website design for a maid or cleaning service.

They have a horrible website that we want turned into a masterpiece.

As you will see on their current site:

http://tidyharborco.examplehost.net/

They have a lot of stuff, very disorganized, and need help.

Here is what we need:

Colors: Same as current site, Orange, Gray, Black

Menu: Horizontal with same Menu items

Need a spot for a video on the homepage

Want content to be structured in a great format that is easy to read.

Want to highlight commercial and residential on the website homepage.

Also want a spot for customer testimonials

We want the site clean, professional, fresh and modern.

Please help by matching the logo design.

I look forward to your designs!
Updates

Hi All! Really appreciate your efforts and designs. I will be meeting with our client on Monday and will then be able to provide feedback after our meeting. If you have other ideas, please submit them. The more I can show him the better! Thanks!

Target Market(s)

The target market is residential home owners as well as commercial businesses who need cleaning on a regular basis.

This company cleans homes and offices for individuals.

Industry/Entity Type

Residential

Font styles to use
Sans Serif

Requirements
Must have
• Must match logo colors
Must have spot for video
Must have a clean look
Must have a bold look
Nice to have
• Highly visual
Should not have
• clutter
messy design
hard to read

```html
<!DOCTYPE html>
<html lang="en">
<head>
<meta charset="utf-8">
<title>Tidy Harbor — Quality Commercial &amp; Residential Cleaning</title>
<link href="https://fonts.googleapis.com/css2?family=Open+Sans:wght@400;600;700;800&family=Exo+2:ital,wght@1,900&display=swap" rel="stylesheet">
<style>
  :root {
    --orange: #f07c14;
    --orange-deep: #e0650a;
    --orange-light: #f7a21c;
    --charcoal: #3a3f44;
    --charcoal-dark: #24282b;
    --gray: #58595b;
    --gray-mid: #8e9093;
    --gray-light: #d7d8d9;
    --text: #3c3c3c;
    --white: #ffffff;
  }
  * { box-sizing: border-box; margin: 0; padding: 0; }
  html, body { width: 1148px; height: 1200px; overflow: hidden; background: var(--white); }
  body { font-family: "Open Sans", Arial, sans-serif; color: var(--text); }
  .page { position: relative; width: 1148px; height: 1200px; overflow: hidden; background: var(--white); }

  .top-strip { position: absolute; left: 0; top: 0; width: 100%; height: 12px; background: var(--orange); }

  .ceo-tab { position: absolute; left: 778px; top: 12px; width: 260px; height: 40px; }
  .ceo-tab span { position: absolute; inset: 0; display: flex; align-items: center; justify-content: center;
    color: var(--white); font-size: 14px; font-weight: 400; letter-spacing: 0.2px; }

  .brand { position: absolute; left: 112px; top: 62px; }
  .brand-name { display: flex; align-items: center; gap: 12px;
    font-size: 38px; font-weight: 800; color: var(--gray); letter-spacing: -0.5px; line-height: 1; }
  .brand-mark { width: 30px; height: 30px; background: var(--orange); }
  .brand-tagline { margin-top: 10px; margin-left: 42px; font-size: 13px; font-weight: 600; color: var(--gray-mid); }

  .call { position: absolute; left: 794px; top: 72px; font-size: 22px; font-weight: 700; color: var(--gray); }
  .call b { color: var(--orange); }

  .search { position: absolute; left: 799px; top: 118px; width: 232px; height: 36px;
    border: 1px solid var(--gray-light); background: var(--white); }
  .search span { position: absolute; left: 13px; top: 8px; font-size: 13px; color: #777; }
  .search svg { position: absolute; right: 8px; top: 5px; }

  .main-nav { position: absolute; left: 0; top: 187px; width: 100%; height: 53px;
    background: linear-gradient(#4d5358, var(--charcoal) 55%, var(--charcoal-dark)); }
  .main-nav ul { list-style: none; display: flex; justify-content: space-between;
    position: absolute; left: 115px; width: 912px; top: 17px; }
  .main-nav li { color: var(--white); font-size: 14.5px; font-weight: 400; }
  .main-nav li.is-active { color: var(--orange-light); }

  .hero-band { position: absolute; left: 0; top: 240px; width: 100%; height: 433px;
    background: linear-gradient(180deg, var(--orange) 0%, var(--orange-deep) 45%, #ee8a12 80%, #f3a320 100%); }
  .hero-band::after { content: ""; position: absolute; left: 0; bottom: 0; width: 100%; height: 70px;
    background: repeating-linear-gradient(90deg, rgba(255,255,255,0.05) 0 2px, rgba(0,0,0,0.04) 2px 4px); }
  .hero-rule { position: absolute; left: 0; top: 678px; width: 100%; height: 2px; background: var(--gray-light); }

  .slider { position: absolute; left: 113px; top: 257px; width: 915px; height: 377px;
    background: var(--white); padding: 6px; }
  .slide-photo { position: relative; width: 100%; height: 100%;
    background: linear-gradient(100deg, #9a6a3e 0%, #d9c9b6 30%, #ece6de 55%, #5a4a40 80%, #e8e4dd 100%); }
  .slide-caption { position: absolute; left: 0; bottom: 0; width: 100%; height: 72px;
    background: rgba(20,20,20,0.85); display: flex; align-items: center; justify-content: center; text-align: center; }
  .slide-caption p { font-family: "Exo 2", "Arial Black", sans-serif; font-style: italic; font-weight: 900;
    font-size: 28px; line-height: 29px; color: var(--orange); text-transform: uppercase; letter-spacing: 0.3px; }
  .slider-arrow { position: absolute; top: 431px; width: 25px; height: 30px; background: var(--white);
    border-radius: 3px; display: flex; align-items: center; justify-content: center; }
  .slider-arrow.prev { left: 90px; }
  .slider-arrow.next { left: 1027px; }

  .service-tabs { position: absolute; left: 98px; top: 710px; }
  .service-tabs text { font-family: "Open Sans", Arial, sans-serif; font-weight: 700; font-size: 22px;
    letter-spacing: 2px; fill: var(--white); }

  .welcome { position: absolute; left: 101px; top: 813px; width: 400px; }
  .welcome h1 { font-size: 29px; font-weight: 700; letter-spacing: 2.4px; color: var(--gray); line-height: 1;
    white-space: nowrap; text-transform: uppercase; }
  .welcome h1 span { color: var(--orange); }
  .welcome p { margin-top: 19px; font-size: 13.2px; line-height: 19px; color: var(--text); }
  .welcome p + p { margin-top: 19px; }
  .welcome a { color: var(--orange); text-decoration: none; }

  .video { position: absolute; left: 546px; top: 864px; width: 499px; height: 280px;
    background: #8c8d8f; padding: 9px 9px 0; }
  .video-frame { width: 100%; height: 226px;
    background: linear-gradient(120deg, #e9e4e0 0%, #f1d94a 35%, #e0508a 55%, #6cc7d6 72%, #ecebe8 100%); }
  .video-controls { position: absolute; left: 2px; right: 2px; bottom: 0; height: 40px;
    background: linear-gradient(#3d4044, #232527); }
  .video-reflection { position: absolute; left: 546px; top: 1146px; width: 499px; height: 44px;
    background: linear-gradient(rgba(140,141,143,0.35), rgba(255,255,255,0)); }
</style>
</head>
<body>
<div class="page">
  <div class="top-strip"></div>

  <div class="ceo-tab">
    <svg width="260" height="40" viewBox="0 0 260 40" aria-hidden="true">
      <polygon points="0,0 260,0 248,40 12,40" fill="var(--orange)"/>
    </svg>
    <span>MEET THE PRESIDENT &amp; CEO</span>
  </div>

  <div class="brand">
    <div class="brand-name"><span class="brand-mark"></span>Tidy Harbor</div>
    <div class="brand-tagline">Quality Commercial &amp; Residential Cleaning</div>
  </div>

  <div class="call"><b>Call:</b> (505) 555-0182</div>

  <div class="search">
    <span>Search</span>
    <svg width="26" height="26" viewBox="0 0 26 26" aria-hidden="true">
      <circle cx="10" cy="10" r="7.5" fill="none" stroke="#9a9a9a" stroke-width="2"/>
      <line x1="15.5" y1="15.5" x2="23" y2="23" stroke="#9a9a9a" stroke-width="3" stroke-linecap="round"/>
    </svg>
  </div>

  <nav class="main-nav">
    <ul>
      <li class="is-active">HOME</li>
      <li>ABOUT US</li>
      <li>SERVICES</li>
      <li>EMPLOYEES</li>
      <li>WHY CHOOSE US?</li>
      <li>SPECIAL OFFERS</li>
      <li>REQUEST A BID</li>
      <li>TESTIMONIALS</li>
      <li>CONTACT US</li>
    </ul>
  </nav>

  <div class="hero-band"></div>
  <div class="hero-rule"></div>

  <div class="slider">
    <div class="slide-photo" role="img" aria-label="Bright tidy living room with a leather sofa, wooden floor and shelving">
      <div class="slide-caption">
        <p>Wouldn’t it be nice, to come home to a<br>perfectly clean house?</p>
      </div>
    </div>
  </div>
  <div class="slider-arrow prev">
    <svg width="10" height="14" viewBox="0 0 10 14" aria-hidden="true"><polygon points="8,1 2,7 8,13" fill="var(--orange)"/></svg>
  </div>
  <div class="slider-arrow next">
    <svg width="10" height="14" viewBox="0 0 10 14" aria-hidden="true"><polygon points="2,1 8,7 2,13" fill="var(--orange)"/></svg>
  </div>

  <svg class="service-tabs" width="950" height="60" viewBox="0 0 950 60" aria-label="Services">
    <polygon points="751,0 922,0 946,30 922,59 751,59 775,30" fill="var(--orange)"/>
    <text x="799" y="38">OTHERS</text>
    <polygon points="448,0 751,0 775,30 751,59 448,59 472,30" fill="var(--gray)"/>
    <text x="496" y="38">OFFICE BUILIDINGS</text>
    <polygon points="210,0 448,0 472,30 448,59 210,59 234,30" fill="var(--orange)"/>
    <text x="255" y="38">COMMERCIAL</text>
    <polygon points="0,0 210,0 234,30 210,59 0,59" fill="var(--gray)"/>
    <text x="17" y="38">RESIDENTIAL</text>
  </svg>

  <section class="welcome">
    <h1>Welcome to <span>Tidy Harbor</span></h1>
    <p>Thank you for visiting us! You are one step closer to experiencing first class maid service! Our company specializes in detailed housekeeping, janitorial, and commerical cleaning services making your environment shine and sparkle like it never has before! Our maids are fully trained professionals who we recruit from high end luxury hotels we know, like the Grandview and Larkspur! We pride ourselves in delivering exceptional service to our valued customers by fully understanding what your expectations &amp; needs are!</p>
    <p>We will strive for perfection and we will provide an uncompromising commitment to excellence! Our "Tidy Harbor" name gives us an edge over our competition by giving you access to more home and office cleaning services for absolutely no extra costs! Why pay more for less?? NEVER have any hidden charges, overages, or sneaky fees! With Tidy Harbor start getting more for your dollar! Your wish is our command and that is the true "Tidy Harbor" way! <a href="#">Call us today!</a></p>
  </section>

  <div class="video">
    <div class="video-frame" role="img" aria-label="Video still of a cleaner in yellow gloves holding colourful cleaning bottles"></div>
    <div class="video-controls">
      <svg width="495" height="40" viewBox="0 0 495 40" aria-hidden="true">
        <polygon points="17,12 17,28 30,20" fill="#cfd2d5"/>
        <rect x="48" y="18" width="290" height="4" rx="2" fill="#15171a"/>
        <rect x="48" y="18" width="26" height="4" rx="2" fill="#2aa3e0"/>
        <circle cx="74" cy="20" r="7" fill="#c8cbce"/>
        <polygon points="370,16 375,16 381,11 381,29 375,24 370,24" fill="#cfd2d5"/>
        <circle cx="404" cy="20" r="6" fill="none" stroke="#cfd2d5" stroke-width="3" stroke-dasharray="2.5 1.5"/>
        <circle cx="404" cy="20" r="2" fill="#cfd2d5"/>
        <text x="422" y="26" font-family="Open Sans, Arial, sans-serif" font-weight="800" font-size="15" fill="#2aa3e0">HD</text>
        <path d="M455 13 l5 0 M455 13 l0 5 M455 13 l6 6 M472 13 l-5 0 M472 13 l0 5 M472 13 l-6 6 M455 28 l5 0 M455 28 l0 -5 M455 28 l6 -6 M472 28 l-5 0 M472 28 l0 -5 M472 28 l-6 -6" stroke="#cfd2d5" stroke-width="2" fill="none"/>
      </svg>
    </div>
  </div>
  <div class="video-reflection"></div>
</div>
</body>
</html>
```